Brimwell is a steel frame construction company that builds residential and commercial homes

1. Homepage (we are after a basic website)
Hero Section:
A full-width image or video showcasing steel frames in construction or a finished project.
Tagline: Short, impactful tagline (e.g., "Strong Structures for Tomorrow").
Call-to-Action (CTA): A prominent "Get a Quote" or "Contact Us" button.
About Us (Snapshot Section):

A few lines about the company, emphasizing experience, certifications, and commitment to quality.
Include a "Learn More" button linking to the detailed About Us page.
Products/Services Section:

Feature the main products like steel frames for industrial, residential, and commercial projects.
Each category should have a "Learn More" link to a dedicated product page.
Project Showcase/Portfolio:

Display 2-3 featured projects with images, descriptions, and a "View All Projects" button.
Certifications & Partners:

Display logos of certifications (ISO, local building standards) and partnerships with construction companies or industry bodies.
Footer:

Contact information, quick links (Home, About, Products, Services, Contact), and social media icons.
2. Products Page
Overview:

A grid or list layout showing different steel frame products or services.
Each product should have a title, brief description, and a thumbnail image.
Individual Product Pages:

Detailed information on specific products (e.g., “Steel Frames for Residential Construction”):
Features: Highlight specific features like durability, eco-friendliness, precision, etc.
Technical Specs: Material grades, dimensions, finishes available.
Case Studies: A couple of client testimonials or case studies of where this product was used.
Downloadable Resources:

Technical datasheets or catalogs for users to download.
Include a form to capture user information before they download the document (optional for lead generation).
3. Projects/Portfolio Page
Gallery of Projects:
Display completed projects with high-quality images, each linked to a project detail page.
Filter options (e.g., industrial, residential, commercial).
Project Detail Pages:
A detailed description of the project, challenges, and how the steel frames were used.
other website we liked are:
https://www.brimwellframing.com.au/
https://quorvantframe.com.au/

1. Objective:
Create an informative, professional, and visually appealing website that promotes steel frame construction solutions, showcasing the company’s offerings, expertise, and projects.
The website should highlight the benefits of steel frames (e.g., durability, sustainability, and cost-efficiency) and cater to both B2B and B2C clients.
2. Target Audience:
Primary: Architects, builders, and construction companies.
Secondary: Homeowners, investors, and property developers looking for modern, durable construction solutions.

```html
<!DOCTYPE html>
<html lang="en">
<head>
<meta charset="utf-8">
<title>Brimwell — Steel Frame Construction</title>
<link href="https://fonts.googleapis.com/css2?family=Poppins:wght@400;500;600;700&display=swap" rel="stylesheet">
<style>
:root{
  --brand:#1866b4;
  --brand-dark:#12599f;
  --ink:#222;
  --muted:#555;
  --rule:#9a9a9a;
  --soft:#f4f4f4;
  --white:#fff;
}
*{box-sizing:border-box;margin:0;padding:0}
html,body{width:1200px;height:5004px;overflow:hidden}
body{position:relative;font-family:'Poppins',sans-serif;color:var(--ink);background:var(--white)}
.abs{position:absolute}
.photo{position:absolute;display:block}
.btn{position:absolute;display:flex;align-items:center;justify-content:center;gap:14px;background:var(--brand);color:var(--white);font-weight:600;text-decoration:none;border-radius:40px;letter-spacing:.2px}
.btn svg{display:block}
.eyebrow{position:absolute;left:0;width:1200px;text-align:center;font-size:20px;color:#333;letter-spacing:.5px;display:flex;justify-content:center;align-items:center;gap:16px}
.eyebrow::before,.eyebrow::after{content:"";width:56px;height:2px;background:var(--rule)}
.section-title{position:absolute;left:0;width:1200px;text-align:center;font-size:50px;font-weight:500;color:var(--brand);letter-spacing:1px;line-height:1}

/* header */
.site-header{position:absolute;left:0;top:0;width:1200px;height:93px;background:var(--white)}
.brand{position:absolute;display:flex;align-items:center;gap:10px;font-weight:700;letter-spacing:1px}
.brand .mark{display:block}
.header-brand{left:68px;top:26px;font-size:34px;color:var(--brand)}
.header-brand .mark{width:26px;height:26px;background:var(--brand)}
.main-nav a{position:absolute;top:36px;font-size:14px;color:#333;text-decoration:none}
.main-nav a.active{color:var(--brand)}
.main-nav a.active::after{content:"";position:absolute;left:-4px;right:-4px;top:26px;height:2px;background:var(--brand)}

/* hero */
.hero{position:absolute;left:0;top:93px;width:1200px;height:699px}
.hero-title{position:absolute;left:66px;color:var(--white);font-weight:500;line-height:1;letter-spacing:1px}

/* about */
.about-ring{position:absolute;left:175px;top:913px;width:382px;height:382px;border:3px solid var(--brand);border-radius:50%}
.about-label{position:absolute;left:619px;top:920px;font-size:14px;color:#444;display:flex;align-items:center;gap:8px}
.about-label::after{content:"";width:44px;height:1.5px;background:var(--rule)}
.about-title{position:absolute;left:619px;top:943px;font-size:42px;font-weight:500;color:var(--brand)}
.about-text{position:absolute;left:619px;top:1012px;width:405px;font-size:14px;line-height:28px;color:#333;text-align:justify}

/* services */
.services{position:absolute;left:0;top:1414px;width:1200px;height:878px;background:var(--soft)}
.service-card{position:absolute;top:1662px;width:311px;height:498px;background:var(--white);box-shadow:0 2px 10px rgba(0,0,0,.08)}
.service-card .photo{left:6px;top:6px;width:299px;height:251px}
.service-card h3{position:absolute;top:289px;left:0;width:100%;text-align:center;font-size:20px;font-weight:500;color:var(--brand);letter-spacing:.5px}
.service-card p{position:absolute;top:330px;left:34px;width:243px;font-size:14px;line-height:24px;color:#444;text-align:center}
.service-card .btn{left:95px;top:437px;width:121px;height:27px;font-size:10px;gap:6px}

/* featured */
.feature-caption{position:absolute;top:3938px;width:340px;font-size:20px;font-weight:500;line-height:30px;color:var(--ink)}

/* partners */
.slider-arrow{position:absolute;top:4546px;width:44px;height:44px;border-radius:50%;display:flex;align-items:center;justify-content:center}

/* footer */
.site-footer{position:absolute;left:0;top:4715px;width:1200px;height:289px;background:var(--brand)}
.footer-brand{left:68px;top:80px;font-size:54px;color:var(--white)}
.footer-brand .mark{width:38px;height:38px;border:0;background:var(--white)}
.footer-links{position:absolute;right:66px;top:78px;display:flex;gap:0;font-size:14px;color:var(--white)}
.footer-links a{color:var(--white);text-decoration:none}
.footer-links span{margin:0 18px}
.footer-contact{position:absolute;right:66px;display:flex;align-items:center;gap:8px;font-size:14px;color:var(--white)}
.footer-contact svg{display:block}
.footer-bar{position:absolute;left:0;top:245px;width:1200px;height:44px;border-top:1px solid rgba(255,255,255,.35);text-align:center;font-size:12px;line-height:42px;color:var(--white)}
</style>
</head>
<body>

<header class="site-header">
  <div class="brand header-brand"><span class="mark"></span>BRIMWELL</div>
  <nav class="main-nav">
    <a href="#" class="active" style="left:676px">HOME</a>
    <a href="#" style="left:749px">ABOUT US</a>
    <a href="#" style="left:850px">SERVICES ▾</a>
    <a href="#" style="left:939px">PORTFOLIO</a>
    <a href="#" style="left:1046px">CONTACT US</a>
  </nav>
</header>

<section class="hero">
  <div class="photo" role="img" aria-label="Steel frame building facade with glass panels under a cloudy sky" style="left:0;top:0;width:1200px;height:699px;background:linear-gradient(120deg,#3a3d42 0%,#6b6f75 40%,#8a8d91 60%,#4a4d52 100%)"></div>
  <h1 class="hero-title" style="top:228px;font-size:60px">STRONG STRUCTURES</h1>
  <h1 class="hero-title" style="top:305px;font-size:78px">FOR TOMORROW</h1>
  <a href="#" class="btn" style="left:68px;top:437px;width:262px;height:70px;font-size:19px">GET A QUOTE
    <svg width="42" height="10" viewBox="0 0 42 10"><path d="M0 5H40M35 1l5 4-5 4" stroke="#fff" stroke-width="2" fill="none"/></svg></a>
</section>

<section class="about">
  <div class="about-ring"></div>
  <div class="photo" role="img" aria-label="Steel staircase structure seen from below" style="left:193px;top:931px;width:346px;height:346px;border-radius:50%;background:radial-gradient(circle,#cfd6de 0%,#6d7885 60%,#2e3744 100%)"></div>
  <div class="about-label">WHO WE ARE</div>
  <h2 class="about-title">ABOUT US</h2>
  <p class="about-text">Lorem ipsum dolor sit amet, consectetur adipiscing elit. Maecenas in tincidunt risus. Vestibulum consequat tin cidunt eros vitae sollicitudin. Duis at imperdiet leo, nec facilisis ex. Vestibulum sed cursus purus, ut tristique lorem. Vestibulum consequat tincidunt eros vitae sollici tudin. Duis at imperdiet leo, nec facilisis ex. Vestibulum sed cursus purus, ut tristique lorem.</p>
  <a href="#" class="btn" style="left:619px;top:1243px;width:183px;height:47px;font-size:13px;gap:10px">LEARN MORE
    <svg width="40" height="10" viewBox="0 0 40 10"><path d="M0 5H38M33 1l5 4-5 4" stroke="#fff" stroke-width="2" fill="none"/></svg></a>
</section>

<section class="services"></section>
<div class="eyebrow" style="top:1515px">WHAT WE DO</div>
<h2 class="section-title" style="top:1548px">OUR SERVICES</h2>

<article class="service-card" style="left:103px">
  <div class="photo" role="img" aria-label="Industrial steel scaffolding structure" style="background:linear-gradient(160deg,#e6e9ee 0%,#8c96a4 55%,#4c5562 100%)"></div>
  <h3>INDUSTRIAL</h3>
  <p>Lorem ipsum dolor sit amet, consec tetur adipiscing elit, sed do eiusmod tempor incididunt ut labore et dolore</p>
  <a href="#" class="btn">LEARN MORE <svg width="18" height="8" viewBox="0 0 18 8"><path d="M0 4H16M13 1l3 3-3 3" stroke="#fff" stroke-width="1.5" fill="none"/></svg></a>
</article>
<article class="service-card" style="left:445px">
  <div class="photo" role="img" aria-label="Residential apartment building with steel balconies" style="background:linear-gradient(160deg,#c9dbea 0%,#98a7b6 50%,#5e6a78 100%)"></div>
  <h3>RESIDENTIAL</h3>
  <p>Lorem ipsum dolor sit amet, consec tetur adipiscing elit, sed do eiusmod tempor incididunt ut labore et dolore</p>
  <a href="#" class="btn">LEARN MORE <svg width="18" height="8" viewBox="0 0 18 8"><path d="M0 4H16M13 1l3 3-3 3" stroke="#fff" stroke-width="1.5" fill="none"/></svg></a>
</article>
<article class="service-card" style="left:787px">
  <div class="photo" role="img" aria-label="Commercial building with dark glass and steel walkway" style="background:linear-gradient(150deg,#1e2329 0%,#4a525c 50%,#9aa2ab 100%)"></div>
  <h3>COMMERCIAL</h3>
  <p>Lorem ipsum dolor sit amet, consec tetur adipiscing elit, sed do eiusmod tempor incididunt ut labore et dolore</p>
  <a href="#" class="btn">LEARN MORE <svg width="18" height="8" viewBox="0 0 18 8"><path d="M0 4H16M13 1l3 3-3 3" stroke="#fff" stroke-width="1.5" fill="none"/></svg></a>
</article>

<section class="projects">
  <div class="eyebrow" style="top:2393px">PROJECT PORTFOLIO</div>
  <h2 class="section-title" style="top:2426px">OUR PROJECTS</h2>
  <div class="photo" role="img" aria-label="Steel frame facade against a blue sky" style="left:66px;top:2534px;width:526px;height:301px;background:linear-gradient(120deg,#5b6470 0%,#b9c4cf 55%,#7b8591 100%)"></div>
  <div class="photo" role="img" aria-label="Industrial factory interior with steel roof trusses and robotic arms" style="left:606px;top:2534px;width:526px;height:301px;background:linear-gradient(180deg,#e8eaec 0%,#b3b6b9 55%,#a9835a 100%)"></div>
  <div class="photo" role="img" aria-label="Curved steel and glass walkway in sunlight" style="left:66px;top:2849px;width:344px;height:301px;background:linear-gradient(135deg,#eef2f7 0%,#a9b6c7 50%,#5d6f86 100%)"></div>
  <div class="photo" role="img" aria-label="Curved steel staircase railing against a blue wall" style="left:425px;top:2849px;width:346px;height:301px;background:linear-gradient(135deg,#3f74c4 0%,#2b558f 55%,#1b2e4d 100%)"></div>
  <div class="photo" role="img" aria-label="External steel staircase on an orange and grey building" style="left:786px;top:2849px;width:346px;height:301px;background:linear-gradient(135deg,#d7d7d7 0%,#8a8a8a 45%,#c9731f 100%)"></div>
  <a href="#" class="btn" style="left:499px;top:3208px;width:202px;height:60px;font-size:17px">VIEW MORE
    <svg width="32" height="10" viewBox="0 0 32 10"><path d="M0 5H30M25 1l5 4-5 4" stroke="#fff" stroke-width="2" fill="none"/></svg></a>
</section>

<section class="featured">
  <div class="eyebrow" style="top:3483px">BRIMWELL</div>
  <h2 class="section-title" style="top:3515px">FEATURED PROJECTS</h2>
  <div class="photo" role="img" aria-label="Blue steel stair on a modern clad building" style="left:68px;top:3626px;width:336px;height:277px;background:linear-gradient(135deg,#3a4a63 0%,#d3cdb8 50%,#a8927a 100%)"></div>
  <div class="photo" role="img" aria-label="Yellow building facade with black steel balcony" style="left:431px;top:3626px;width:338px;height:277px;background:linear-gradient(90deg,#6e7d8a 0%,#c8d0d6 40%,#e0b12a 75%,#d19a18 100%)"></div>
  <div class="photo" role="img" aria-label="Brick apartment building with steel balconies and fire escape" style="left:794px;top:3626px;width:338px;height:277px;background:linear-gradient(90deg,#8a7a6e 0%,#6b5a4e 40%,#a5583a 75%,#8d4a30 100%)"></div>
  <p class="feature-caption" style="left:68px">Lorem ipsum dolor sit amet, con sectetur adipiscing elit, sed do eiusmod tempor</p>
  <p class="feature-caption" style="left:431px">Lorem ipsum dolor sit amet, con sectetur adipiscing elit, sed do eiusmod tempor</p>
  <p class="feature-caption" style="left:794px">Lorem ipsum dolor sit amet, con sectetur adipiscing elit, sed do eiusmod tempor</p>
  <a href="#" class="btn" style="left:466px;top:4082px;width:268px;height:58px;font-size:17px">VIEW ALL PROJECTS
    <svg width="30" height="10" viewBox="0 0 30 10"><path d="M0 5H28M23 1l5 4-5 4" stroke="#fff" stroke-width="2" fill="none"/></svg></a>
</section>

<section class="partners">
  <div class="eyebrow" style="top:4364px">BRIMWELL CLIENTS</div>
  <h2 class="section-title" style="top:4397px">CERTIFICATIONS &amp; PARTNERS</h2>
  <div class="slider-arrow" style="left:69px;background:#a9a9a9">
    <svg width="12" height="14" viewBox="0 0 12 14"><path d="M8 2L3 7l5 5" stroke="#fff" stroke-width="2" fill="none"/></svg></div>
  <div class="abs" role="img" aria-label="Certification badge" style="left:193px;top:4520px;width:110px;height:102px;background:var(--brand)"></div>
  <div class="abs" role="img" aria-label="Partner badge" style="left:545px;top:4522px;width:74px;height:78px;border-radius:0 0 37px 37px;background:#d2452a"></div>
  <div class="abs" role="img" aria-label="Partner badge" style="left:717px;top:4510px;width:120px;height:120px;border-radius:50%;background:var(--brand)"></div>
  <div class="abs" role="img" aria-label="Partner badge" style="left:928px;top:4520px;width:78px;height:78px;background:#7a2a2a"></div>
  <div class="slider-arrow" style="left:1091px;background:var(--brand)">
    <svg width="12" height="14" viewBox="0 0 12 14"><path d="M4 2l5 5-5 5" stroke="#fff" stroke-width="2" fill="none"/></svg></div>
</section>

<footer class="site-footer">
  <div class="brand footer-brand"><span class="mark"></span>BRIMWELL</div>
  <nav class="footer-links">
    <a href="#">HOME</a><span>|</span><a href="#">ABOUT US</a><span>|</span><a href="#">SERVICES</a><span>|</span><a href="#">PORTFOLIO</a><span>|</span><a href="#">CONTACT US</a>
  </nav>
  <div class="footer-contact" style="top:122px">
    <svg width="18" height="18" viewBox="0 0 18 18"><rect width="18" height="18" rx="3" fill="#fff"/><path d="M4 6h10v7H4zM4 6l5 4 5-4" stroke="#1866b4" stroke-width="1.3" fill="none"/></svg>
    <span>info@websitename.com</span>
    <svg width="18" height="18" viewBox="0 0 18 18" style="margin-left:10px"><rect width="18" height="18" rx="3" fill="#fff"/><path d="M6 4c-1 1-1 3 1 6s4 4 5 4l1.5-1.5-2-2-1 1c-1-.5-2.5-2-3-3l1-1-2-2z" fill="#1866b4"/></svg>
    <span>+012 345 6789</span>
  </div>
  <div class="footer-contact" style="top:166px">
    <svg width="18" height="18" viewBox="0 0 18 18"><rect width="18" height="18" rx="3" fill="#fff"/><path d="M9 3.5a3.5 3.5 0 0 0-3.5 3.5c0 2.6 3.5 7 3.5 7s3.5-4.4 3.5-7A3.5 3.5 0 0 0 9 3.5z" fill="#1866b4"/><circle cx="9" cy="7" r="1.2" fill="#fff"/></svg>
    <span>Address line Dummy Here, Address line Here</span>
  </div>
  <div class="footer-bar">Copyright © 2024 All Rights Reserved By Company Name</div>
</footer>

</body>
</html>
```